Brochure Design Project

1.We need a brochure design for our event program and invitation.

2.We must be able to print out the brochure and also send it out via email to participants.

3.We want the whole design to relate to "Cross-Examination","International Arbitration" atmosphere.

4.We want the design to look a bit (but not too) fancy and be readable.

Reason: There are only 2 of 6 designs we like. But we still need more options to choose.

Target Market(s)

Our audiences are all Chinese and International Lawyers

Industry/Entity Type

Event

Requirements
Must have
• 1. The brochure needs to actually reflect “cross-examination” on the cover. The title should go at the top of the page.

2. The brochure needs to make room for organizers and supporters’ logo. This is a cooperation event.

3. It is important that the text is a big enough to be read easily. At the moment we have been using Helvetica font at size 9 or 10. Helvetica is easily readable at this size.

4. The brochure color needs to be in line with our logo color, such as Green-Blue and white. Please suggest a color that also fits the organizers’ logo.

5. We need a pdf version and print out version. They are all A4 size. The pdf version size must be under 2 MB. Otherwise it’s difficult to send out as well as receive. For the printing version, when designing you need to leave a 4mm bleed over the page size. This bleed is important - otherwise the picture will not necessarily go to the edge of the cut. You also need to make sure that the text is not too close to the boundary. I tend to leave a 4-5mm margin for text within this on all sides.

6. Use the same font style as suggested in the draft program and invitation.
Nice to have
• A picture which represents the idea of cross-examination. I will send you the example pic.
Should not have
• 1. Should not be aggressive;

2. Should not be too fancy or too conservative;

3. Should not be too colorful

```html
<!DOCTYPE html>
<html lang="en">
<head>
<meta charset="utf-8">
<title>Registration Form – Cross-Examination Workshop</title>
<link href="https://fonts.googleapis.com/css2?family=Arimo:ital,wght@0,400;0,700;1,400;1,700&display=swap" rel="stylesheet">
<style>
  :root{
    --ink:#5a5a5a;
    --green:#2e9e6e;
    --green-deep:#23875c;
    --mint:#d7ece2;
    --mist:#ececec;
    --paper:#ffffff;
  }
  *{margin:0;padding:0;box-sizing:border-box}
  html,body{width:846px;height:1200px;overflow:hidden;background:var(--paper)}
  .page{position:relative;width:846px;height:1200px;overflow:hidden;background:var(--paper);
    font-family:"Arimo",Helvetica,Arial,sans-serif;color:var(--ink);font-size:13.5px;line-height:21.5px}
  .swoosh{position:absolute;inset:0;width:846px;height:1200px}
  .content{position:relative;padding:16px 46px 0 54px}
  .line{white-space:nowrap}
  .box{display:inline-block;width:10px;height:10px;border:1px solid var(--ink);margin:0 4px 0 0;vertical-align:-1px}
  .blank{display:inline-block;width:44px;border-bottom:1px solid var(--ink);margin:0 3px;height:13px;vertical-align:-1px}
  .blank.wide{width:600px}
  .blank.long{width:220px}
  .gap{display:inline-block;width:34px}
  .green{color:var(--green-deep);font-weight:700}
  .section-title{font-style:italic;font-weight:700;font-size:16px;color:#666;margin-top:12px}
  .para{white-space:normal;width:740px}
  .signature{margin-top:26px;text-align:right;padding-right:14px}
</style>
</head>
<body>
<div class="page">
  <svg class="swoosh" viewBox="0 0 846 1200" aria-hidden="true">
    <path d="M0 40 C200 120 360 520 380 1200 L300 1200 C290 620 150 230 0 150 Z" fill="var(--mist)"/>
    <path d="M0 170 C170 260 300 640 320 1200 L210 1200 C200 720 120 380 0 300 Z" fill="var(--mint)"/>
    <path d="M0 250 C150 360 250 700 270 1200 L180 1200 C170 780 100 470 0 390 Z" fill="var(--green)" opacity="0.92"/>
    <path d="M0 0 C120 20 220 80 300 170" stroke="var(--mint)" stroke-width="3" fill="none"/>
  </svg>

  <div class="content">
    <div class="line">You have acted as: <span class="box"></span>Counsel for<span class="blank"></span>times <span class="box"></span>Arbitrator for<span class="blank"></span>times</div>
    <div class="line"><span class="box"></span>Expert and / or witness for<span class="blank"></span>times</div>
    <div class="line">At which Arbitration Commissions:</div>
    <div class="line"><span class="box"></span>CIDRC <span class="box"></span>Northgate Arbitration Commission<span class="gap"></span><span class="box"></span>Eastport Arbitration Commission</div>
    <div class="line"><span class="box"></span>Others<span class="blank wide"></span></div>
    <div class="line green">- Experience of Arbitration outside China:</div>
    <div class="line">How many times have you been involved in arbitration outside China? <span class="box"></span>0 <span class="box"></span>1-5 <span class="box"></span>5-15</div>
    <div class="line"><span class="box"></span>More than 15</div>
    <div class="line">You have acted as: <span class="box"></span>Counsel for<span class="blank"></span>times <span class="box"></span>Arbitrator for<span class="blank"></span>times</div>
    <div class="line"><span class="box"></span>Expert and / or witness for<span class="blank"></span>times</div>
    <div class="line">At which Arbitration Commissions:</div>
    <div class="line"><span class="box"></span>Ad hoc Arbitration<span class="gap"></span><span class="box"></span>IDC <span class="box"></span>HKDRC <span class="box"></span>SDRC<span class="gap"></span><span class="box"></span>NCC <span class="box"></span>Alpine Rules <span class="box"></span>IRSD</div>
    <div class="line"><span class="box"></span>Others<span class="blank wide"></span></div>
    <div class="line green">- Have you ever examined a witness / expert before?</div>
    <div class="line"><span class="box"></span>Yes for<span class="blank"></span>times <span class="box"></span>No</div>

    <div class="section-title">Declaration:</div>
    <p class="para">I declare that the above information is correct and understand that the information will be added to the database of the organizers and sponsors. The organizers may make use of my information for promotion purposes in relation to the Event. I accept that the organizers bear no responsibility for any errors or omissions.</p>

    <div class="section-title">Fee:</div>
    <div class="line">Early booking fee:</div>
    <div class="line"><span class="box"></span>RMB 3500 / person (for registrations completed prior to or on 15 October 2012)</div>
    <div class="line">Standard booking fee (for registrations completed after 15 October 2012):</div>
    <div class="line"><span class="box"></span>RMB 4,500 / person</div>
    <p class="para">(In case of registration of several people from a same law firm or organization, we are able to provide you with the following discounts: RMB 8,500 for 2 people, RMB 12,000 for 3 people, and RMB 16,000 for 4 people. Please fill out 1 registration form per person and send them jointly to VerdanARB for joint processing)</p>
    <div class="line"><i>The fee includes:</i></div>
    <p class="para">1) Attendance of the 1½ Days workshop 2) Attendance of the lunch &amp; dinner 3) Personal coaching by senior instructors 4) Support materials 5) Obtention upon course completion of a NTAI Certificate</p>
    <div class="line">Upon receipt of your registration and the registration fee, you will receive a registration confirmation.</div>

    <div class="section-title">Cancellation Policy</div>
    <div class="line">Cancellation charges are as follows:</div>
    <div class="line">Cancellation prior to or on 15 October 2012: full refund (minus 5.6% processing charge)</div>
    <div class="line">Cancellation after 15 October 2012 and prior to 30 November 2012: 50% refund</div>
    <div class="line">Cancellation after 1 December 2012: No refund*</div>
    <p class="para">- Where no refund is granted, the payer keeps a credit of the paid amount with VerdanARB and may use this credit for attendance of a future event.</p>

    <div class="section-title">Enquiries:</div>
    <p class="para">For further information for the event, please contact with VerdanARB:<br>Tel: +86 10 5550 1234 or Email: event@verdanarb.com</p>
    <p class="para"><span class="box"></span>I hereby register for the VerdanARB - Harbor Point Arbitration Chambers International, llc International Arbitration Event. Please inform me of future events of <span class="box"></span>VerdanARB or <span class="box"></span>Harbor Point Arbitration Chambers International, llc.</p>

    <div class="line signature">Signature:<span class="blank long"></span>Date :<span class="blank long"></span></div>
  </div>
</div>
</body>
</html>
```